I'm an electrician and the name of my company is called Brisk 'N' Bright Electrical. I require a professional business card that speaks to my clients, I also need it to be innovative and modern. We do maintenance & service work for domestic and commercial premises.

Industry/Entity Type

Electrical

Contact Information for Business Card

Must have the name of my company Brisk 'N' Bright Electrical, my name Darren Kolovos and my contact details 0427 381 592 and company email address Brisknbrightelectrical@mailvane.com and/or website Brisknbrightelectrical.com.au

Logo Text

Brisk 'N' Bright Electrical (If possible)

Colors
33a6d7
0592cd
3176b5

```html
<!DOCTYPE html>
<html lang="en">
<head>
<meta charset="utf-8">
<title>Brisk 'N' Bright Electrical – Business Card</title>
<link rel="stylesheet" href="https://fonts.googleapis.com/css2?family=Roboto:wght@400;500&display=swap">
<style>
  :root {
    --stage: #2e3133;
    --card-front: #0b0c0d;
    --card-back: #0e101c;
    --accent: #33a6d7;
    --accent-mid: #0592cd;
    --accent-deep: #3176b5;
    --ink: #ffffff;
    --icon-ink: #0b1520;
  }
  * { margin: 0; padding: 0; box-sizing: border-box; }
  html, body { width: 1200px; height: 1000px; overflow: hidden; }
  body {
    background: var(--stage);
    font-family: "Roboto", Arial, sans-serif;
    color: var(--ink);
    position: relative;
  }
  .card {
    position: absolute;
    overflow: hidden;
    box-shadow: 0 4px 10px rgba(0,0,0,0.45);
  }
  .card-front { left: 350px; top: 67px; width: 718px; height: 410px; background: var(--card-front); }
  .card-back  { left: 133px; top: 522px; width: 716px; height: 410px; background: var(--card-back); }
  .card-art { position: absolute; inset: 0; width: 100%; height: 100%; }

  .company-title {
    position: absolute; left: 0; right: 0; top: 44px;
    text-align: center; font-weight: 400; font-size: 28px; letter-spacing: 1.4px;
  }
  .holder-name {
    position: absolute; left: 68px; top: 120px;
    font-weight: 500; font-size: 26px;
  }
  .contact-list { position: absolute; left: 68px; top: 173px; list-style: none; }
  .contact-item {
    display: flex; align-items: center; height: 40px; margin-bottom: 15px;
    font-size: 19px; letter-spacing: 0.3px;
  }
  .contact-icon { width: 40px; height: 40px; margin-right: 13px; flex: none; }

  .brand-mark {
    position: absolute; left: 229px; top: 78px; width: 256px; height: 256px;
    border-radius: 50%;
    background: #1a1d24;
    border: 12px solid var(--accent);
    display: flex; flex-direction: column; align-items: center; justify-content: center;
    text-align: center;
    font-weight: 500; font-size: 25px; line-height: 1.3; letter-spacing: 1px;
    color: var(--ink);
  }
</style>
</head>
<body>

<section class="card card-front" aria-label="Business card front">
  <svg class="card-art" viewBox="0 0 718 410" aria-hidden="true">
    <defs>
      <linearGradient id="ringFade" x1="0" y1="0" x2="0" y2="1">
        <stop offset="0" stop-color="#33a6d7" stop-opacity="0"/>
        <stop offset="1" stop-color="#33a6d7"/>
      </linearGradient>
      <linearGradient id="ringFadeUp" x1="0" y1="1" x2="0" y2="0">
        <stop offset="0" stop-color="#33a6d7" stop-opacity="0"/>
        <stop offset="1" stop-color="#33a6d7"/>
      </linearGradient>
      <pattern id="dotsFront" width="10" height="10" patternUnits="userSpaceOnUse">
        <circle cx="2.5" cy="2.5" r="1.9" fill="#fff"/>
      </pattern>
      <linearGradient id="stripeFront" x1="0" y1="1" x2="1" y2="0">
        <stop offset="0" stop-color="#3176b5" stop-opacity="0"/>
        <stop offset="1" stop-color="#3176b5"/>
      </linearGradient>
    </defs>
    <circle cx="70" cy="83" r="45" fill="none" stroke="url(#ringFadeUp)" stroke-width="8"/>
    <circle cx="480" cy="161" r="38" fill="none" stroke="url(#ringFade)" stroke-width="6"/>
    <circle cx="358" cy="348" r="31" fill="none" stroke="url(#ringFade)" stroke-width="6"/>
    <rect x="630" y="49" width="45" height="150" fill="url(#dotsFront)"/>
    <rect x="33" y="351" width="120" height="33" fill="url(#dotsFront)"/>
    <polygon points="718,198 718,215 495,410 476,410" fill="url(#stripeFront)"/>
    <polygon points="718,228 718,410 508,410" fill="var(--accent-mid)"/>
  </svg>

  <h1 class="company-title">BRISK 'N' BRIGHT ELECTRICAL</h1>
  <p class="holder-name">Darren Kolovos</p>
  <ul class="contact-list">
    <li class="contact-item">
      <svg class="contact-icon" viewBox="0 0 40 40" aria-hidden="true">
        <circle cx="20" cy="20" r="20" fill="var(--accent)"/>
        <path d="M13 12c2-2 4 0 5 2s0 3-1 4c1 2 3 4 5 5 1-1 2-2 4-1s4 3 2 5c-2 2-6 2-10-2s-7-9-5-13z" fill="var(--icon-ink)"/>
      </svg>
      0427 381 592
    </li>
    <li class="contact-item">
      <svg class="contact-icon" viewBox="0 0 40 40" aria-hidden="true">
        <circle cx="20" cy="20" r="20" fill="var(--accent)"/>
        <rect x="10" y="13" width="20" height="14" fill="var(--icon-ink)"/>
        <path d="M10 13l10 8 10-8" fill="none" stroke="var(--accent)" stroke-width="1.4"/>
      </svg>
      Brisknbrightelectrical@mailvane.com
    </li>
    <li class="contact-item">
      <svg class="contact-icon" viewBox="0 0 40 40" aria-hidden="true">
        <circle cx="20" cy="20" r="20" fill="var(--accent)"/>
        <g fill="none" stroke="var(--icon-ink)" stroke-width="1.8">
          <circle cx="20" cy="20" r="9"/>
          <ellipse cx="20" cy="20" rx="4" ry="9"/>
          <path d="M11 20h18M13 15h14M13 25h14"/>
        </g>
      </svg>
      Brisknbrightelectrical.com.au
    </li>
  </ul>
</section>

<section class="card card-back" aria-label="Business card back">
  <svg class="card-art" viewBox="0 0 716 410" aria-hidden="true">
    <defs>
      <linearGradient id="ringBack" x1="0" y1="0" x2="1" y2="0">
        <stop offset="0" stop-color="#33a6d7" stop-opacity="0"/>
        <stop offset="1" stop-color="#33a6d7"/>
      </linearGradient>
      <linearGradient id="ringBackUp" x1="0" y1="1" x2="1" y2="0">
        <stop offset="0" stop-color="#33a6d7" stop-opacity="0"/>
        <stop offset="1" stop-color="#33a6d7"/>
      </linearGradient>
      <pattern id="dotsBack" width="10" height="10" patternUnits="userSpaceOnUse">
        <circle cx="2.5" cy="2.5" r="1.9" fill="#fff"/>
      </pattern>
      <linearGradient id="stripeBack" x1="0" y1="1" x2="1" y2="0">
        <stop offset="0" stop-color="#3176b5" stop-opacity="0"/>
        <stop offset="1" stop-color="#3176b5"/>
      </linearGradient>
    </defs>
    <polygon points="168,0 150,0 0,140 0,158" fill="url(#stripeBack)"/>
    <polygon points="0,0 150,0 0,140" fill="var(--accent-mid)"/>
    <circle cx="159" cy="128" r="35" fill="none" stroke="url(#ringBack)" stroke-width="7"/>
    <circle cx="585" cy="178" r="52" fill="none" stroke="url(#ringBack)" stroke-width="8"/>
    <circle cx="222" cy="350" r="45" fill="none" stroke="url(#ringBackUp)" stroke-width="7"/>
    <rect x="543" y="48" width="122" height="33" fill="url(#dotsBack)"/>
    <rect x="37" y="342" width="115" height="33" fill="url(#dotsBack)"/>
    <polygon points="716,224 716,240 536,410 518,410" fill="url(#stripeBack)"/>
    <polygon points="716,248 716,410 545,410" fill="var(--accent-mid)"/>
  </svg>

  <div class="brand-mark">
    <span>BRISK 'N' BRIGHT</span>
    <span>ELECTRICAL</span>
  </div>
</section>

</body>
</html>
```